Small company security and risk consulting startup needs an explosive message via marketing colla...

Need a two page (front/back) flyer that calls out our three primary service areas incorporating tallyquill developed logo and website visuals. Something that grabs attention at first glance to entice the viewer to read and connect for a services consultation. I will need the ability to make minor adjustments and add language.

```html
<!DOCTYPE html>
<html lang="en">
<head>
<meta charset="utf-8">
<title>MeridianGuard – Two-Page Flyer</title>
<link href="https://fonts.googleapis.com/css2?family=Montserrat:wght@500;700;800&family=Lato:wght@400;700&display=swap" rel="stylesheet">
<style>
  :root{
    --bg:#2b2b2b;
    --red:#d0101f;
    --blue:#0e3a94;
    --navy:#0b2a6b;
    --ink:#1a1a1a;
    --footer:#161616;
    --text:#2a2a2a;
    --white:#ffffff;
  }
  *{margin:0;padding:0;box-sizing:border-box}
  html,body{width:1200px;height:1200px;overflow:hidden;background:var(--bg)}
  body{position:relative;font-family:'Lato',sans-serif;color:var(--text)}

  .page{position:absolute;top:205px;width:560px;height:790px;background:var(--white);overflow:hidden;box-shadow:0 10px 30px rgba(0,0,0,.45)}
  .page--front{left:30px}
  .page--back{left:610px}

  .photo{position:absolute;left:0;top:0;width:560px}
  .page--front .photo{height:450px;background:linear-gradient(120deg,#f1eeec 0%,#d9d2cf 35%,#7c7f8c 62%,#3a3e4f 100%)}
  .page--back .photo{height:260px;background:linear-gradient(110deg,#c9d3e2 0%,#e9eef5 45%,#f7f9fc 70%,#dfe5ee 100%)}

  .shapes{position:absolute;left:0;top:0;width:560px;height:790px}

  /* brand */
  .brand{position:absolute;left:28px;top:72px}
  .brand__name{font-family:'Montserrat',sans-serif;font-weight:800;font-size:26px;color:var(--red);display:flex;align-items:center;gap:8px}
  .brand__name::before{content:"";width:14px;height:14px;background:var(--red)}

  .hero{position:absolute;left:28px;top:160px;width:300px}
  .hero__title{font-family:'Montserrat',sans-serif;font-weight:700;font-size:29px;line-height:1.05}
  .hero__title .accent{color:var(--red);display:block}
  .hero__title .dark{color:var(--ink);display:block}
  .hero__text{font-size:11px;line-height:1.3;margin-top:8px;color:#333}

  /* services */
  .service{position:absolute;text-align:center;width:170px}
  .service__shape{display:block;margin:0 auto}
  .service__title{font-family:'Montserrat',sans-serif;font-weight:700;font-size:12px;color:var(--blue);line-height:1.15;margin-top:14px;text-transform:uppercase}
  .service__text{font-size:12px;line-height:1.3;color:var(--text);margin-top:4px}
  .service--security{left:22px;top:500px}
  .service--risk{left:195px;top:510px}
  .service--consult{left:368px;top:455px}

  /* footer */
  .footer{position:absolute;left:0;bottom:0;width:560px;height:88px;background:var(--footer);color:var(--white);font-size:12px}
  .contact{position:absolute;left:40px;top:16px;line-height:19px}
  .contact__row{display:flex;align-items:center;gap:8px}
  .contact__row svg{width:11px;height:11px;flex:none}
  .address{position:absolute;right:36px;top:16px;display:flex;align-items:center;gap:8px}
  .address svg{width:12px;height:14px}

  /* back content */
  .section-title{position:absolute;left:0;width:560px;text-align:center;font-family:'Montserrat',sans-serif;font-weight:800;font-size:19px;color:var(--blue);letter-spacing:.5px}
  .section-title::after{content:"";display:block;width:80px;height:2px;background:var(--red);margin:5px auto 0}
  .section-text{position:absolute;left:40px;width:480px;text-align:center;font-size:10.5px;line-height:1.35;color:var(--text)}
  .section-text p+p{margin-top:8px}
  .about-title{top:270px}
  .about-text{top:305px}
  .why-title{top:420px}
  .why-text{top:455px}

  .review{position:absolute;left:34px;top:565px;width:380px}
  .review__title{font-family:'Montserrat',sans-serif;font-weight:700;font-size:14px;line-height:1.25;color:var(--blue)}
  .review__text{font-size:11.5px;line-height:1.35;margin-top:8px}
  .badge{position:absolute;right:36px;top:555px}
</style>
</head>
<body>

<!-- FRONT PAGE -->
<section class="page page--front">
  <div class="photo" role="img" aria-label="Photo of two business consultants reviewing a tablet at a meeting table"></div>
  <svg class="shapes" viewBox="0 0 560 790" aria-hidden="true">
    <polygon points="0,440 260,470 560,400 560,790 0,790" fill="#f6f6f7"/>
    <polyline points="0,436 260,466 560,396" fill="none" stroke="var(--red)" stroke-width="5"/>
    <polygon points="300,702 560,660 560,702" fill="var(--red)"/>
  </svg>

  <div class="brand">
    <div class="brand__name">MeridianGuard</div>
  </div>

  <div class="hero">
    <h1 class="hero__title"><span class="accent">LOREM IPSUM</span><span class="dark">DOLOR SIT AMET</span></h1>
    <p class="hero__text">consectetur adipiscing elit, sed do eiusmod tempor incididunt ut labore et dolore magna aliqua. Augue eget arcu dictum varius</p>
  </div>

  <div class="service service--security">
    <svg class="service__shape" width="150" height="80" viewBox="0 0 150 80">
      <polygon points="50,0 100,0 150,80 0,80" fill="var(--ink)"/>
      <g fill="none" stroke="#fff" stroke-width="2">
        <rect x="57" y="26" width="36" height="24" rx="2"/>
        <line x1="75" y1="50" x2="75" y2="57"/><line x1="66" y1="57" x2="84" y2="57"/>
        <path d="M63 38 Q75 28 87 38 Q75 48 63 38Z"/><circle cx="75" cy="38" r="3.5"/>
      </g>
    </svg>
    <h2 class="service__title">National<br>Security</h2>
    <p class="service__text">Urna nec tincidunt praesent semper feugiat.</p>
  </div>

  <div class="service service--risk">
    <svg class="service__shape" width="150" height="90" viewBox="0 0 150 90">
      <polygon points="0,0 150,0 95,90 55,90" fill="var(--red)"/>
      <g fill="none" stroke="#fff" stroke-width="2">
        <circle cx="75" cy="38" r="14"/><circle cx="75" cy="38" r="5"/>
        <line x1="75" y1="18" x2="75" y2="24"/><line x1="75" y1="52" x2="75" y2="58"/>
        <line x1="55" y1="38" x2="61" y2="38"/><line x1="89" y1="38" x2="95" y2="38"/>
      </g>
    </svg>
    <h2 class="service__title">Risk Management<br>Services</h2>
    <p class="service__text">Urna nec tincidunt praesent semper feugiat.</p>
  </div>

  <div class="service service--consult">
    <svg class="service__shape" width="150" height="85" viewBox="0 0 150 85">
      <polygon points="45,0 95,0 150,85 0,85" fill="var(--blue)"/>
      <g fill="none" stroke="#fff" stroke-width="2">
        <rect x="58" y="22" width="22" height="15" rx="2"/>
        <rect x="70" y="34" width="22" height="15" rx="2"/>
        <circle cx="75" cy="62" r="6"/>
      </g>
    </svg>
    <h2 class="service__title">Consulting<br>Services</h2>
    <p class="service__text">Urna nec tincidunt praesent semper feugiat.</p>
  </div>

  <footer class="footer">
    <div class="contact">
      <div class="contact__row"><svg viewBox="0 0 12 12"><path d="M2 1h3l1 3-2 1q1 2 3 3l1-2 3 1v3q-8 0-9-9z" fill="#fff"/></svg>(555) 014 3870</div>
      <div class="contact__row"><svg viewBox="0 0 12 12"><rect x="1" y="3" width="10" height="7" fill="#fff"/><polyline points="1,3 6,7 11,3" fill="none" stroke="#161616"/></svg>info@meridianguard.example</div>
      <div class="contact__row"><svg viewBox="0 0 12 12"><circle cx="6" cy="6" r="5" fill="none" stroke="#fff"/><ellipse cx="6" cy="6" rx="2" ry="5" fill="none" stroke="#fff"/><line x1="1" y1="6" x2="11" y2="6" stroke="#fff"/></svg>www.meridianguard.example</div>
    </div>
    <div class="address"><svg viewBox="0 0 12 14"><path d="M6 13C2 8 1 6 1 5a5 5 0 0 1 10 0c0 1-1 3-5 8z" fill="none" stroke="#fff" stroke-width="1.4"/><circle cx="6" cy="5" r="1.8" fill="#fff"/></svg>48 Alder Row, Suite 3, Fairview 40210</div>
  </footer>
</section>

<!-- BACK PAGE -->
<section class="page page--back">
  <div class="photo" role="img" aria-label="Photo of hands pointing at charts on a tablet screen"></div>
  <svg class="shapes" viewBox="0 0 560 790" aria-hidden="true">
    <polygon points="0,235 300,262 560,195 560,790 0,790" fill="#fff"/>
    <polyline points="0,231 300,258 560,191" fill="none" stroke="var(--red)" stroke-width="5"/>
    <polygon points="40,548 540,520 540,526 60,552" fill="#8d8f94" opacity=".55"/>
    <polygon points="300,702 560,660 560,702" fill="var(--red)"/>
  </svg>

  <h2 class="section-title about-title">ABOUT US</h2>
  <div class="section-text about-text">
    <p>Lorem ipsum dolor sit amet, consectetur adipiscing elit, sed do eiusmod tempor incididunt ut labore et dolore magna aliqua. Augue eget arcu dictum varius. Faucibus et molestie ac feugiat sed lectus vestibulum mattis ullamcorper. Rutrum tellus pellentesque eu tincidunt tortor aliquam. In cursus turpis massa tincidunt dui. Etiam tempor orci eu lobortis elementum nibh tellus molestie nunc.</p>
    <p>Odio eu feugiat pretium nibh ipsum consequat nisl. Adipiscing elit duis tristique sollicitudin nibh sit amet commodo nulla. Sodales neque sodales ut etiam sit amet nisl purus in.</p>
  </div>

  <h2 class="section-title why-title">WHY WE ARE</h2>
  <div class="section-text why-text">
    <p>Lorem ipsum dolor sit amet, consectetur adipiscing elit, sed do eiusmod tempor incididunt ut labore et dolore magna aliqua. Augue eget arcu dictum varius. Faucibus et molestie ac feugiat sed lectus vestibulum mattis ullamcorper. Rutrum tellus pellentesque eu tincidunt tortor aliquam.</p>
  </div>

  <div class="review">
    <h3 class="review__title">The decision-macking process of<br>the Strategic Defence and Security Review</h3>
    <p class="review__text">Urna nec tincidunt praesent semper feugiat. Sit amet tellus cras adipiscing enim eu turpis egestas. Nunc congue nisi vitae suscipit tellus. Venenatis a condimentum vitae sapien. Id volutpat lacus laoreet non curabitur gravida arcu ac tortor.</p>
  </div>

  <svg class="badge" width="92" height="80" viewBox="0 0 92 80" role="img" aria-label="Certification badge">
    <circle cx="46" cy="40" r="36" fill="none" stroke="var(--navy)" stroke-width="6"/>
    <circle cx="46" cy="40" r="24" fill="#fff" stroke="var(--red)" stroke-width="2"/>
  </svg>

  <footer class="footer">
    <div class="contact">
      <div class="contact__row"><svg viewBox="0 0 12 12"><path d="M2 1h3l1 3-2 1q1 2 3 3l1-2 3 1v3q-8 0-9-9z" fill="#fff"/></svg>(555) 014 3870</div>
      <div class="contact__row"><svg viewBox="0 0 12 12"><rect x="1" y="3" width="10" height="7" fill="#fff"/><polyline points="1,3 6,7 11,3" fill="none" stroke="#161616"/></svg>info@meridianguard.example</div>
      <div class="contact__row"><svg viewBox="0 0 12 12"><circle cx="6" cy="6" r="5" fill="none" stroke="#fff"/><ellipse cx="6" cy="6" rx="2" ry="5" fill="none" stroke="#fff"/><line x1="1" y1="6" x2="11" y2="6" stroke="#fff"/></svg>www.meridianguard.example</div>
    </div>
    <div class="address"><svg viewBox="0 0 12 14"><path d="M6 13C2 8 1 6 1 5a5 5 0 0 1 10 0c0 1-1 3-5 8z" fill="none" stroke="#fff" stroke-width="1.4"/><circle cx="6" cy="5" r="1.8" fill="#fff"/></svg>48 Alder Row, Suite 3, Fairview 40210</div>
  </footer>
</section>

</body>
</html>
```